Rollin’ Kites Copper Tide beer can design

We are not looking for a new logo, we want to use our current logo!! Current Logo is Attached. We want to incorporate our current logo into a full can design for our new non-alcoholic, THC infused Beer design. We cannot use animals or cartoons. We also can not say beer. We would like to use our main label found at www.rollinkites-example.com
Several ideas include having small images of beer cans and beer mugs all over the can as a background. Another idea is to make it freedom and liberty themed. We want to make sure people understand it is a beer, even though we can say beer on the can.

Target Market(s)

30-50 year olds

Industry/Entity Type

THC beverage

Logo Text

Rollin’ Kites Copper Tide

Colors
59FF00
82FF00
B8FF75
E3FFCB
F4FFEA

Requirements
Must have
• Full 12 oz beer can design
Should not have
• No word beer, do not need a new logo, need a can design

```html
<!DOCTYPE html>
<html lang="en">
<head>
<meta charset="utf-8">
<title>Rollin’ Kites Copper Tide – Can Design</title>
<link rel="stylesheet" href="https://fonts.googleapis.com/css2?family=Montserrat:wght@500;600&family=Roboto+Condensed:wght@400;700&family=Libre+Franklin:wght@400;500;700;900&display=swap">
<style>
  :root{
    --bg:#d4d4d4;
    --can-white:#f6f6f4;
    --rim:#c99a57;
    --rim-dark:#9a6a2e;
    --band:#e07a17;
    --band-dark:#c9600f;
    --brew-light:#f5c542;
    --brew:#f0a418;
    --brew-deep:#e0801a;
    --foam:#fbf4e2;
    --ink:#1c1c1c;
    --brand-ink:#2e5a26;
    --white:#ffffff;
  }
  *{box-sizing:border-box;margin:0;padding:0}
  html,body{width:1200px;height:900px;overflow:hidden;background:var(--bg)}
  .canvas{position:relative;width:1200px;height:900px;background:var(--bg)}

  .can{position:absolute;top:140px;width:260px;height:674px}
  .can--front{left:312px}
  .can--back{left:643px}

  .can__rim{position:absolute;left:28px;right:28px;height:16px;border-radius:8px;
    background:linear-gradient(90deg,var(--rim-dark),var(--rim) 30%,#f0d6a6 55%,var(--rim) 80%,var(--rim-dark))}
  .can__rim--top{top:0}
  .can__rim--bottom{bottom:0}

  .can__body{position:absolute;top:12px;bottom:12px;left:0;right:0;overflow:hidden;
    border-radius:34px 34px 10px 10px;background:var(--can-white)}

  .can__brew{position:absolute;left:0;right:0;top:190px;bottom:0;
    background:linear-gradient(180deg,rgba(251,244,226,0) 0%,var(--foam) 18%,var(--brew-light) 30%,var(--brew) 62%,var(--brew-deep) 100%)}

  .band{position:absolute;left:0;right:0;top:58px;height:26px;
    background:linear-gradient(90deg,var(--band-dark),var(--band) 50%,var(--band-dark));
    border-top:1.5px solid #f4b062;border-bottom:1.5px solid #f4b062;
    display:flex;justify-content:space-between;align-items:center;padding:0 10px;
    font-family:"Montserrat",sans-serif;font-weight:600;font-size:11.5px;color:var(--white);letter-spacing:.2px}

  .brand{position:absolute;left:22px;right:22px;top:84px;height:220px;
    display:flex;flex-direction:column;align-items:center;justify-content:center;gap:10px}
  .brand__mark{width:16px;height:16px;border-radius:50%;background:var(--brand-ink)}
  .brand__name{font-family:"Montserrat",sans-serif;font-weight:600;font-size:24px;line-height:1.2;
    color:var(--brand-ink);text-align:center}

  .tagline{position:absolute;left:0;right:0;top:446px;text-align:center;
    font-family:"Roboto Condensed",sans-serif;font-weight:400;font-size:27px;color:var(--white);letter-spacing:-.3px}

  .volume{position:absolute;left:0;right:0;top:575px;height:28px;
    border-top:1.5px solid #f7c66a;border-bottom:1.5px solid #f7c66a;
    display:flex;align-items:center;justify-content:center;
    font-family:"Montserrat",sans-serif;font-weight:600;font-size:16px;color:var(--white)}
  .base-band{position:absolute;left:0;right:0;bottom:0;height:44px;
    background:linear-gradient(180deg,var(--brew-deep),var(--band-dark))}

  .facts{position:absolute;left:39px;top:78px;width:197px;height:550px;background:var(--white);
    border:2px solid var(--ink);outline:1px solid var(--white);padding:4px 5px;
    font-family:"Libre Franklin",sans-serif;color:var(--ink)}
  .facts__juice{font-size:12px;font-weight:500;border-bottom:1px solid var(--ink);padding-bottom:1px}
  .facts__title{font-size:22.5px;font-weight:900;line-height:1.15;letter-spacing:-.2px;border-bottom:1px solid var(--ink)}
  .facts__serving{display:flex;justify-content:space-between;font-size:11.5px;font-weight:700;padding:2px 0 1px}
  .rule-thick{height:9px;background:var(--ink)}
  .rule-mid{height:4px;background:var(--ink)}
  .facts__amount{font-size:10px;font-weight:700;margin-top:3px}
  .facts__calories{display:flex;justify-content:space-between;font-size:21px;font-weight:900;line-height:1;padding-bottom:3px}
  .facts__dv{text-align:right;font-size:9.5px;font-weight:700;padding:3px 0 2px;border-bottom:1px solid var(--ink)}
  .row{display:flex;justify-content:space-between;font-size:10.5px;line-height:16.2px;border-bottom:1px solid var(--ink)}
  .row b{font-weight:700}
  .row--sub{padding-left:9px}
  .row--subsub{padding-left:20px}
  .row--last{border-bottom:none}
  .facts__note{font-size:6.6px;line-height:1.3;padding:3px 0 4px;border-bottom:1.5px solid var(--ink)}
  .facts__ingredients{font-size:8.2px;line-height:1.45;padding-top:6px;padding-right:18px}
  .facts__ingredients b{font-size:10px;font-weight:700}
</style>
</head>
<body>
<main class="canvas">

  <section class="can can--front" aria-label="Front of can">
    <div class="can__rim can__rim--top"></div>
    <div class="can__body">
      <div class="can__brew" role="img" aria-label="Golden sparkling brew with foam head and rising bubbles"></div>
      <div class="band"><span>NON ALCOHOLIC.</span><span>NON ALCOHOLIC.</span></div>
      <div class="brand">
        <span class="brand__mark"></span>
        <span class="brand__name">Rollin’ Kites<br>Copper Tide</span>
      </div>
      <p class="tagline">“TASTE THE NEW BUZZ”</p>
      <div class="base-band"></div>
      <p class="volume">330ml / 11.1oz</p>
    </div>
    <div class="can__rim can__rim--bottom"></div>
  </section>

  <section class="can can--back" aria-label="Back of can">
    <div class="can__rim can__rim--top"></div>
    <div class="can__body">
      <div class="can__brew" role="img" aria-label="Golden sparkling brew with foam head and rising bubbles"></div>
      <div class="band"><span>NON ALCOHOLIC.</span><span>NON ALCOHOLIC.</span></div>
      <div class="base-band"></div>

      <div class="facts">
        <p class="facts__juice">20% Juice</p>
        <h2 class="facts__title">Nutrition Facts</h2>
        <p class="facts__serving"><span>Serving size</span><span>12 fl. oz.</span></p>
        <div class="rule-thick"></div>
        <p class="facts__amount">Amount per serving</p>
        <p class="facts__calories"><span>Calories</span><span>35</span></p>
        <div class="rule-mid"></div>
        <p class="facts__dv">% Daily Value*</p>
        <p class="row"><span><b>Total Fat</b> 0g</span><b>0%</b></p>
        <p class="row row--sub"><span>Saturated Fat 0g</span><b>0%</b></p>
        <p class="row row--sub"><span>Trans Fat 0g</span><b>0%</b></p>
        <p class="row"><span><b>Cholesterol</b> 0mg</span><b>0%</b></p>
        <p class="row"><span><b>Sodium</b> 0mg</span><b>0%</b></p>
        <p class="row"><span><b>Total Carbohydrate</b> 8g</span><b>3%</b></p>
        <p class="row row--sub"><span>Dietary Fiber 0g</span><b>0%</b></p>
        <p class="row row--sub"><span>Total Sugars 5g</span><span></span></p>
        <p class="row row--subsub"><span>Includes 4g Added Sugars</span><b>8%</b></p>
        <p class="row row--last"><span><b>Protein</b> 0g</span><span></span></p>
        <div class="rule-thick"></div>
        <p class="row"><span>Vitamin D 0mcg</span><span>0%</span></p>
        <p class="row"><span>Calcium 7mg</span><span>0%</span></p>
        <p class="row"><span>Iron 0mg</span><span>0%</span></p>
        <p class="row row--last"><span>Potassium 81mg</span><span>2%</span></p>
        <div class="rule-mid"></div>
        <p class="facts__note">*The % Daily Value tells you how much a nutrient in a serving of food contributes to a daily diet. 2,000 calories a day is used for general nutrition advice.</p>
        <p class="facts__ingredients"><b>Ingredients:</b> Filtered Carbonated Water, Lemon Juice Concentrate, Agave Syrup, Natural Flavor, Water soluble hemp emulsion, (Natural Flavors, Vegetable Oil, Hemp Extract, Ascorbic Acid, Gluconic Acid, Sodium Benzoate, Sucrose Acetate, Isobutyrate), Potassium Sorbate (to preserve freshness), Sucralose.</p>
      </div>
    </div>
    <div class="can__rim can__rim--bottom"></div>
  </section>

</main>
</body>
</html>
```